Homepage graphic for Black Friday Deals

I am wanting a graphic design to promote the upcoming Black Friday deals for my ecommerce store.
The Black Friday deal will be 10% discount off every product in our online store on the Friday 25th, this must be stated on the design. It will also need the text....'Apply coupon code 'BLACKFRIDAY' at the checkout'. Try and fit the design into the current colour scheme whilst also making it fit into the 'Black Friday' theme. I have included images of our top selling products so please try and include as many as these as possible. Be creative and feel free to include anything else that you feel will look good.
The size needs to be: 1150 pixels wide, 402 pixels high.
The website is www.tivanmoulds.co.uk if you need to collect anymore information from there.

```html
<!DOCTYPE html>
<html lang="en">
<head>
<meta charset="utf-8">
<title>Black Friday Super Sale Banner</title>
<link rel="stylesheet" href="https://fonts.googleapis.com/css2?family=Montserrat:wght@300;400;500;600&family=Arimo:wght@700&display=swap">
<style>
  :root {
    --page-bg: #ececec;
    --sale-orange: #ef5022;
    --sale-orange-dark: #d9441a;
    --sale-blue: #3896d3;
    --wood-light: #d8c7b0;
    --wood-mid: #c2ab8d;
    --wood-dark: #a68c6d;
    --tag-yellow: #ffff00;
    --ink: #111111;
    --white: #ffffff;
  }
  * { margin: 0; padding: 0; box-sizing: border-box; }
  html, body {
    width: 1200px;
    height: 1200px;
    overflow: hidden;
    background: var(--page-bg);
  }
  .banner {
    position: absolute;
    left: 25px;
    top: 399px;
    width: 1150px;
    height: 402px;
    overflow: hidden;
    background: var(--sale-orange);
    font-family: "Montserrat", sans-serif;
    color: var(--white);
  }
  .banner-shapes {
    position: absolute;
    inset: 0;
    width: 1150px;
    height: 402px;
  }
  .headline {
    position: absolute;
    left: 121px;
    top: 44px;
    line-height: 1;
  }
  .headline-kicker {
    display: block;
    font-size: 21px;
    font-weight: 400;
    letter-spacing: -0.2px;
  }
  .headline-main {
    display: block;
    font-size: 62px;
    font-weight: 500;
    line-height: 0.78;
    letter-spacing: 1px;
    margin-top: 10px;
  }
  .headline-sub {
    display: block;
    font-size: 35px;
    font-weight: 300;
    margin-top: 6px;
    letter-spacing: 0.5px;
  }
  .headline-sub strong { font-weight: 600; }
  .coupon {
    position: absolute;
    left: 336px;
    top: 275px;
    width: 300px;
    text-align: center;
    line-height: 1;
  }
  .coupon-label {
    display: block;
    font-size: 18px;
    font-weight: 500;
  }
  .coupon-code {
    display: block;
    font-size: 34px;
    font-weight: 500;
    color: var(--ink);
    margin-top: 14px;
  }
  .coupon-note {
    display: block;
    font-size: 18px;
    font-weight: 500;
    margin-top: 4px;
  }
  .discount-tag {
    position: absolute;
    left: 798px;
    top: 31px;
    width: 352px;
    height: 56px;
    background: var(--tag-yellow);
    box-shadow: 0 2px 5px rgba(0,0,0,0.3);
    font-family: "Arimo", sans-serif;
    font-weight: 700;
    font-size: 31px;
    color: var(--ink);
    display: flex;
    align-items: center;
    justify-content: center;
    letter-spacing: 0.3px;
  }
</style>
</head>
<body>
  <section class="banner">
    <svg class="banner-shapes" viewBox="0 0 1150 402" xmlns="http://www.w3.org/2000/svg">
      <defs>
        <linearGradient id="woodFill" x1="0" y1="0" x2="1" y2="1">
          <stop offset="0" stop-color="var(--wood-mid)"/>
          <stop offset="0.5" stop-color="var(--wood-light)"/>
          <stop offset="1" stop-color="var(--wood-dark)"/>
        </linearGradient>
      </defs>
      <polygon class="seam-shade" points="0,369 591,144 0,402" fill="var(--sale-orange-dark)" opacity="0.5"/>
      <polygon class="seam-lower" points="0,376 591,144 794,402 0,402" fill="var(--sale-orange)"/>
      <polygon class="panel-blue" points="0,0 483,0 591,144 168,302 0,89" fill="var(--sale-blue)"/>
      <polygon class="product-photo" role="img" aria-label="Photo of top-selling waterproofing tubs, sealant tubes, adhesives and cleaning wipes on a curved wooden plank floor"
               points="483,0 1150,0 1150,402 794,402 591,144" fill="url(#woodFill)"/>
    </svg>

    <h1 class="headline">
      <span class="headline-kicker">LIMITED TIME ONLY</span>
      <span class="headline-main">BLACK<br>FRIDAY</span>
      <span class="headline-sub">SUPER <strong>SALE</strong></span>
    </h1>

    <p class="coupon">
      <span class="coupon-label">APPLY COUPON CODE</span>
      <span class="coupon-code">‘BLACKFRIDAY’</span>
      <span class="coupon-note">AT CHECKOUT</span>
    </p>

    <div class="discount-tag">ALL ITEMS 10% OFF</div>
  </section>
</body>
</html>
```